Flyer für Lettershop
Zielgruppe
Informationen entnehmen Sie bitte: http://www.postfunk-versand.example
Aufgabenstellung
Entwurf eines 6-Seiter Flyer. Dieser soll später als Selfmailer verschickt werden.
Eine grobe Vorstellung entnehmen Sie bitte dem Anhang. Dies soll nur eine kleine Inspiration sein, Sie müssen sich nicht an diese Vorlage halten.
Drei Hauptprodukte bieten wir an: Kuvertierte Mailings (Formate: DIN-L, C5, C4 - Maschine Travolin KX-4700), Postkarten und Selfmailer. Wir möchten das die Preise ins Auge fallen, trotsdem bieten wir eine perfekte und professionelle Qualität.
Informationen und Bilder können Sie postfunk-versand.example entnehmen.
Texte auf Wunsch auch von unserem Subunternehmen: http://www.briefwerk-satz.example/about-us/
Sollten Sie Fragen oder Wünsche haben, zögern Sie bitte nicht uns zu kontaktieren.

```html
<!DOCTYPE html>
<html lang="de">
<head>
<meta charset="utf-8">
<title>Flyer Lettershop – postfunk versand</title>
<link rel="stylesheet" href="https://fonts.googleapis.com/css2?family=Open+Sans:wght@400;600;700;800&family=Montserrat:wght@700;800&display=swap">
<style>
  :root{
    --orange:#f39200;
    --band:#58585a;
    --ink:#2b2b2b;
    --text:#3a3a3a;
    --box:#c9c9ca;
    --tab:#b4b5b8;
    --rule:#a9a9ab;
    --paper:#ffffff;
    --stage:#ffffff;
  }
  *{box-sizing:border-box;margin:0;padding:0}
  html,body{width:1200px;height:803px;overflow:hidden;background:var(--stage)}
  body{position:relative;font-family:"Open Sans",Arial,sans-serif;color:var(--text)}

  .sheet{position:absolute;background:var(--paper);box-shadow:0 4px 10px rgba(0,0,0,.18)}
  .sheet::before,.sheet::after{content:"";position:absolute;left:0;right:0;background:var(--band)}
  .sheet::before{top:0;height:8px}
  .sheet::after{bottom:0;height:10px}

  /* ---------- Außenseite ---------- */
  .outer{left:20px;top:170px;width:590px;height:420px}
  .panel-pro{position:absolute;left:14px;top:22px;width:170px;font-size:7.8px;line-height:10.1px}
  .panel-pro h2,.panel-about h2{font-size:11px;font-weight:700;color:var(--ink);margin-bottom:7px}
  .rule{border-top:1px solid var(--rule);margin:10px 0 6px}
  .benefits{list-style:none;color:var(--orange);font-weight:700}
  .benefits li::before{content:"";display:inline-block;width:4px;height:4px;background:var(--orange);margin-right:3px;vertical-align:1px}
  .contact-box{position:absolute;left:0;top:282px;width:182px;height:92px;background:var(--box);padding:6px 14px;font-size:7.8px;line-height:10.1px}
  .contact-box .mail{color:var(--orange);font-weight:700;font-size:9px}
  .contact-box .phone{color:var(--orange);font-weight:700;font-size:12.5px;margin-top:2px}
  .contact-box p+p{margin-top:9px}
  .web{position:absolute;left:14px;top:392px;font-size:8px;font-weight:700;color:var(--orange)}

  .badge{position:absolute;left:218px;top:30px;width:46px;height:82px;border:1px solid #cfcfcf;border-radius:4px;background:#f4f4f4}
  .bubble{position:absolute;left:283px;top:42px;width:92px;height:92px}
  .bubble-text{position:absolute;left:288px;top:52px;width:80px;height:70px;display:flex;align-items:center;justify-content:center;transform:rotate(-72deg);color:#fff;font-weight:700;font-size:8.4px;line-height:9.6px;text-align:center}
  .vert{position:absolute;writing-mode:vertical-rl;transform:rotate(180deg);white-space:nowrap}
  .brand{left:206px;top:150px;height:190px;font-size:23px;font-weight:400;color:var(--band);letter-spacing:.5px;line-height:28px}
  .brand-sub{left:236px;top:150px;height:193px;font-size:10.5px;line-height:13px;color:var(--band)}
  .brand-mark{position:absolute;left:214px;top:352px;width:18px;height:18px;background:var(--orange)}
  .address{left:262px;top:300px;height:90px;font-size:9px;line-height:11.5px;color:var(--ink)}

  .panel-about{position:absolute;left:410px;top:22px;width:168px;font-size:7.8px;line-height:10.1px}
  .panel-about p+p{margin-top:9px}
  .photo{position:absolute;top:352px;width:81px;height:43px}
  .photo.machine{left:407px;background:linear-gradient(135deg,#8d8f92,#d9dadb 55%,#4a4b4d)}
  .photo.feeder{left:493px;background:linear-gradient(135deg,#2e2d2b,#8c8a86 50%,#d8d4cc)}

  /* ---------- Angebote ---------- */
  .offers{left:640px;top:14px;width:540px;height:772px}
  .offer{position:absolute;left:0;right:0;height:240px}
  .offer:nth-child(1){top:26px}
  .offer:nth-child(2){top:272px}
  .offer:nth-child(3){top:516px}
  .tab{position:absolute;left:0;top:0;width:120px;height:32px;background:var(--tab);color:var(--orange);font-weight:700;font-style:italic;font-size:12.5px;padding:8px 0 0 30px}
  .offer .line{position:absolute;left:120px;right:0;top:30px;border-top:1px solid var(--rule)}
  .offer h3{position:absolute;left:30px;top:52px;font-family:"Montserrat",Arial,sans-serif;font-weight:800;font-size:14px;letter-spacing:.3px;color:#444}
  .specs{position:absolute;left:28px;top:86px;width:240px;font-size:10.3px;line-height:12.6px;color:var(--ink)}
  .sample{position:absolute;left:275px;top:30px;width:195px;height:150px;background:linear-gradient(160deg,#f6f6f7,#e6e8eb 60%,#d6dde6)}
  .sample::before{content:"";position:absolute;left:60px;right:10px;top:10px;height:3px;background:#c2185b}
  .sample::after{content:"";position:absolute;left:0;right:40px;bottom:18px;height:4px;background:#1f6fb2}
  .price{position:absolute;left:382px;top:110px;width:130px;height:100px;background:var(--orange);border-radius:34px 40px 46px 10px;color:#fff;padding:14px 0 0 14px}
  .price .qty{font-weight:700;font-size:10.5px}
  .price .amount{font-weight:800;font-size:21px;line-height:26px;margin-top:2px}
  .price .note{font-weight:600;font-size:10px}
</style>
</head>
<body>

<section class="sheet outer" aria-label="Flyer Außenseite">
  <div class="panel-pro">
    <h2>Was spricht für uns?</h2>
    <p>Postfunk versand und seine Mitarbeiter blicken auf langjährige Erfahrung zurück und bieten den Kunden die Gewissheit, dass Mailings kompetent und zuverlässig, professionell und zeitgenau bei größt­möglicher Kostenoptimierung platziert werden.</p>
    <div class="rule"></div>
    <ul class="benefits">
      <li>30 Jahre Erfahrung</li>
      <li>Großer Maschinenpark</li>
      <li>Inhaber geführtes Unternehmens</li>
      <li>Langjähriger Mitarbeiterstamm</li>
      <li>Preisgünstig</li>
      <li>Modernste EDV und Software Lösung</li>
      <li>Große Lagerkapazität</li>
    </ul>
    <div class="rule"></div>
    <p>Wir binden unsere Kunden durch die Qualität, die wir abliefern.<br>Sollte diese den Ansprüchen des Kunden nicht genügen, haben wir ihn nicht ver­dient.</p>
  </div>
  <div class="contact-box">
    <p>Sie wünschen eine individuelle Beratung, eine persönliche Betreuung und die kom­petente Realisierung? Schreiben Sie uns eine EMail an:<br><span class="mail">info@postfunk-versand.example</span></p>
    <p>oder Rufen Sie uns an:</p>
    <div class="phone">0211 – 555 019-0</div>
  </div>
  <div class="web">www.postfunk-versand.example</div>

  <div class="badge" aria-hidden="true"></div>
  <svg class="bubble" viewBox="0 0 92 92" aria-hidden="true">
    <circle cx="49" cy="44" r="43" fill="#b4b5b8"/>
    <circle cx="45" cy="46" r="43" fill="var(--orange)"/>
  </svg>
  <div class="bubble-text">Wir haben die kleinen Preise im Mailingversand!</div>

  <div class="vert brand">postfunk versand</div>
  <div class="vert brand-sub">Service für Dialogmarketing GmbH</div>
  <div class="brand-mark" aria-hidden="true"></div>
  <div class="vert address">postfunk versand<br>Lindenweg 12<br>40210 Musterstadt</div>

  <div class="panel-about">
    <h2>Über uns</h2>
    <p>Wir bieten unseren Kunden den kom­pletten Lettershop Service mit all seinen Facetten an, vom Laserauftrag bis zur Portooptimierten Postauflieferung.</p>
    <p>Sprechen Sie uns an, wenn Sie eine Wer­beaussendung oder ein Mailing planen. Publikationen einmalig oder regelmäßig versenden wollen oder anderweitig den direkten Weg zu Ihren Kunden suchen und hierfür fachliches Know-how benö­tigen. Die individuelle Beratung, die per­sönliche Betreuung und die kompetente Realisierung Ihrer Wünsche sind bei uns in besten Händen, zuverlässig und kos­tenoptimiert.</p>
    <p>Kurzfristig abzuwickelnde Großaufträge oder kleine Auflagen zwischendurch, wir stehen unseren Kunden mit unsere Let­tershop-Erfahrung gleichberechtigt und immer vollumfänglich zur Verfügung. Unsere Referenzen sind erstklassig.</p>
    <p>Unternehmen aus ganz unterschiedlichen Bereichen greifen immer wieder zufrieden auf unsere Mitarbeit zurück. Für uns das sichere Zeichen, dass unsere Leistung, unser Know-how und unsere Fachkompe­tenz Anerkennung finden.</p>
  </div>
  <div class="photo machine" role="img" aria-label="Foto einer Kuvertiermaschine mit Papierstapel"></div>
  <div class="photo feeder" role="img" aria-label="Foto der Zuführung einer Lettershop-Maschine"></div>
</section>

<section class="sheet offers" aria-label="Flyer Angebote">
  <article class="offer">
    <div class="tab">//Angebot 1:</div><div class="line"></div>
    <h3>BRIEFMAILING DIN-L AUFLAGE</h3>
    <p class="specs">Datenübernahme,<br>Druck A4 Briefbogen 4/0-farbig 90 gm²,<br>Druck A4 Flyer 4/4-farbig 135 gm²,<br>Personalisieren &amp; Text- Lasern schwarz 1-seitig,<br>Briefhüllen C6/5 mit Fenster ohne Druck,<br>Falzen, Kuvertieren 2 Teile maschinell,<br>Postauflieferen</p>
    <div class="sample" role="img" aria-label="Muster eines DIN-lang Mailings mit Briefbogen und Umschlag"></div>
    <div class="price"><div class="qty">5.000 Stück</div><div class="amount">Nur 495,- €</div><div class="note">zzgl. MwSt. + Porto</div></div>
  </article>
  <article class="offer">
    <div class="tab">//Angebot 2:</div><div class="line"></div>
    <h3>KARTENMAILING</h3>
    <p class="specs">Datenübernahme,<br>Druck Maxi Postkarte 260 g/m²<br>23,5 cm x 12,5 cm mit Hochglanz-UV-Lack auf der Vorderseite, Inkjet-Adressieren auf der Rückseite 1/0-farbig schwarz, Postauflieferen</p>
    <div class="sample" role="img" aria-label="Muster einer Maxi-Postkarte"></div>
    <div class="price"><div class="qty">5.000 Stück</div><div class="amount">Nur 295,- €</div><div class="note">zzgl. MwSt. + Porto</div></div>
  </article>
  <article class="offer">
    <div class="tab">//Angebot 3:</div><div class="line"></div>
    <h3>SELFMAILER</h3>
    <p class="specs">Datenübernahme,<br>Druck Selfmailer 170 g/m² matt A4 gefalzt auf DIN lang,<br>6-seiter (Wickelfalz)<br>4/4-farbig, mit zwei transparente, perforierte Klebepunkte verschließen,<br>Inkjet-Adressieren 1-Seitig schwarz,<br>Postauflieferen</p>
    <div class="sample" role="img" aria-label="Muster eines gefalzten 6-seitigen Selfmailers"></div>
    <div class="price"><div class="qty">5.000 Stück</div><div class="amount">Nur 435,- €</div><div class="note">zzgl. MwSt. + Porto</div></div>
  </article>
</section>

</body>
</html>
```